Design a flyer

Hi, I need a flyer designed for an electrical and air conditioning company based in brisbane, Australia.
We service the domestic market.
Flyer is to be double sided
Flyer size DL 210mm X 99mm
Was thinking one side services and discount coupons and the other side possible testimonials.
I have logo uploaded followed with the vehicle advertising, advertising stand alone sign and also business cards.
--------------------------
Coupon Cut out
save $150 OFF switchboard upgrades
save $150 Complimentary Electrical safety inspection
save $50 OFF Air Conditioner install or Service
save $50 next job if you leave feedback for first job
OVER $400 WORTH OF SAVINGS!
Our promise to you
* we will Arrive on time or we will pay you $100
* Before any job begins you will know the exact price
* We will leave your place as clean as we arrived
* if there is a problem and its our fault we will fix it for free
* provide a 12 month warranty on all parts
* we will provide friendly helpful service and advice
Phone number is 0487 562 903
Company Name - Quillbrook
License: 58164
ABN - 61 208 359 772
Also add swift pay, nexo and tapnet logo at the bottom
----------------------------
Here is what some of my customers have had to say
Extremely professional...
“Arrived when he said he would, sent through a written quote and was very reasonable. He also checked out our smoke
detectors whist he was here. He installed 2 ceiling fans and an air conditioner. He
cleaned up the mess and was very efficient. I will definitely use him again and recommend
him to family and friends”
P.M – Stretton
“Excellent service provider. He arrived on time with a call before arriving, than carried all jobs quickly and efficiently and left no mess at all. I will definitely recommend his service to others requiring an electrician. Thanks again!”
R.T – Greenslopes
“Over the long weekend, I had problems with my power, not only did you pick up the first phone call but you came out at 5am to fix it. Love the fact you’re a 24hr service!”
K.L – Mount Gravatt
---------------------------
NEW changes
Hi everyone,
Just want to say well done all the designers look great!
I will soon be choosing a winner, but there are a couple of changes i would like to make, if you revise you will be in for a win.
Instead of Save 50 if you leave feedback for the first job quote. I want to change that put $110 cross out and put $71.50 Install & Supply LED Downlights (min 20)
I want this to be the number one followed by switch board upgrade cut out.
Also $50 off air con install - don't put service.
And the third testimonial K.L Make sure it has a full stop
Also keep in mind. It is an electrical & air conditioning company.
Be creative with your design, don't want to see any pictures of people as they are not working for us at this time.
Remember key focus, on coupons, phone numbers, and website. nexo and swiftpay can be small and out of the way same with the license numbers.
Thank you
Good Luck!
Domestic Market - Home owners
Air Conditioning

```html
<!DOCTYPE html>
<html lang="en">
<head>
<meta charset="utf-8">
<title>Quillbrook – DL Flyer</title>
<link href="https://fonts.googleapis.com/css2?family=Open+Sans:wght@400;600;700;800&family=Oswald:wght@600&family=Dancing+Script:wght@700&display=swap" rel="stylesheet">
<style>
:root{
  --blue:#1f6fb8;
  --blue-light:#2f86cf;
  --blue-dark:#175a99;
  --orange:#e8711f;
  --orange-light:#f39432;
  --ink:#111;
  --paper:#fff;
  --bg:#ece9e4;
}
*{margin:0;padding:0;box-sizing:border-box}
html,body{width:1200px;height:1199px;overflow:hidden}
body{background:var(--bg);font-family:"Open Sans",Arial,sans-serif;position:relative}
.flyer{position:absolute;top:122px;width:450px;height:955px;background:linear-gradient(180deg,var(--blue-light),var(--blue));overflow:hidden;box-shadow:0 6px 18px rgba(0,0,0,.25)}
.flyer--front{left:120px}
.flyer--back{left:630px;background:var(--paper)}
.flyer svg.shape{position:absolute;left:0;top:0}
.brand{position:absolute;left:0;width:100%;text-align:center;display:flex;justify-content:center;align-items:center;gap:10px}
.brand__dot{width:14px;height:14px;border-radius:50%;background:var(--orange)}
.brand__name{font-size:44px;font-weight:400;color:var(--blue);letter-spacing:2px}
.title{position:absolute;top:188px;width:100%;text-align:center;font-weight:800;font-size:41px;line-height:45px;color:var(--ink)}
.sectors{position:absolute;width:100%;text-align:center;font-size:23px;color:var(--ink);font-weight:600}
.sectors .sep{color:var(--orange)}
.savings-head{position:absolute;top:450px;width:100%;text-align:center;color:#fff;font-weight:800;font-size:25px}
.coupons{position:absolute;left:21px;top:492px;width:412px;height:184px;border:3px dashed #fff;display:grid;grid-template-columns:1fr 1fr;grid-template-rows:1fr 1fr}
.coupon{position:relative;color:#fff;text-align:center;padding-top:8px}
.coupon:nth-child(1),.coupon:nth-child(3){border-right:3px dashed #fff}
.coupon:nth-child(1),.coupon:nth-child(2){border-bottom:3px dashed #fff}
.coupon__save{position:absolute;left:10px;top:0;font-family:"Dancing Script",cursive;font-size:30px;color:var(--orange)}
.coupon__amount{font-family:"Oswald",Arial,sans-serif;font-size:29px;line-height:34px;margin-left:30px}
.coupon__amount s{text-decoration-color:var(--orange);text-decoration-thickness:3px}
.coupon__amount .new{font-family:"Dancing Script",cursive;color:var(--orange);font-size:27px}
.coupon__text{font-size:14px;line-height:15px;margin-top:4px}
.promise-head{position:absolute;left:17px;top:700px;color:#fff;font-weight:700;font-size:24px}
.promise{position:absolute;left:20px;top:737px;width:420px;list-style:none;color:#fff;font-size:13.3px;line-height:17px}
.promise li{position:relative;padding-left:22px;margin-bottom:5px}
.promise li::before{content:"";position:absolute;left:2px;top:5px;width:8px;height:8px;border-radius:50%;background:var(--orange)}
.footer{position:absolute;left:0;bottom:0;width:100%;height:80px;background:var(--blue-dark);color:#fff}
.footer__label{position:absolute;left:17px;top:8px;font-size:15px}
.footer__phone{position:absolute;left:17px;top:28px;font-size:21px;font-weight:700;display:flex;align-items:center;gap:7px}
.footer__web{position:absolute;left:17px;top:54px;font-size:14px}
.pay{position:absolute;right:14px;top:10px;display:flex;gap:3px}
.pay span{width:50px;height:34px;background:#fff;color:var(--blue-dark);font-size:11px;font-weight:700;display:flex;align-items:center;justify-content:center}
.legal{position:absolute;right:14px;top:58px;font-size:10px}
.flyer--back .footer{height:84px;background:transparent}
.banner{position:absolute;left:30px;top:232px;width:422px;height:74px;background:var(--orange);color:#fff;font-size:22px;line-height:24px;padding:10px 0 0 8px;font-weight:600}
.testimonials{position:absolute;left:22px;top:330px;width:420px;display:flex;flex-direction:column;gap:18px}
.review{position:relative;background:var(--blue);color:#fff;font-size:13px;line-height:17px;padding:8px 10px 10px 16px}
.review::after{content:"";position:absolute;left:0;bottom:-22px;border-top:22px solid var(--blue-dark);border-left:22px solid transparent}
.review__mark{font-size:46px;font-weight:800;line-height:24px;vertical-align:-14px;margin-right:6px}
.review__who{margin:5px 0 0 30px;color:var(--orange);font-weight:700;font-size:14px;line-height:19px}
</style>
</head>
<body>

<section class="flyer flyer--front">
  <svg class="shape" width="450" height="955" viewBox="0 0 450 955">
    <path d="M0 28 C120 -5 240 10 330 60 L450 60 L450 0 L0 0Z" fill="var(--blue)"/>
    <path d="M0 34 C120 8 230 22 320 72 C210 42 110 40 0 60Z" fill="var(--orange)"/>
    <path d="M0 60 C110 40 210 42 320 72 C380 70 420 64 450 60 L450 382 C330 420 160 420 0 385Z" fill="var(--paper)"/>
    <path d="M0 385 C160 420 330 420 450 382 L450 400 C330 435 150 435 0 410Z" fill="var(--orange)"/>
  </svg>
  <div class="brand" style="top:108px"><span class="brand__name">Quillbrook</span><span class="brand__dot"></span></div>
  <h1 class="title">ELECTRICAL &amp;<br>AIR CONDITIONAL<br>SERVICES</h1>
  <p class="sectors" style="top:332px">Domestic <span class="sep">•</span> Commercial</p>
  <p class="sectors" style="top:361px">Install <span class="sep">•</span> Service <span class="sep">•</span> Maintenance</p>

  <h2 class="savings-head">OVER $400 WORTH OF SAVINGS</h2>
  <div class="coupons">
    <div class="coupon"><span class="coupon__save">Save</span><div class="coupon__amount" style="margin-left:50px"><s>$110</s> <span class="new">$71.50</span></div><p class="coupon__text">Install &amp; Supply<br>LED Downlights (min 20)</p></div>
    <div class="coupon"><span class="coupon__save">Save</span><div class="coupon__amount">$150 OFF</div><p class="coupon__text" style="margin-top:10px">Swithboard upgrades</p></div>
    <div class="coupon"><span class="coupon__save">Save</span><div class="coupon__amount">$150</div><p class="coupon__text">Complimentary Electrical<br>safety inspection</p></div>
    <div class="coupon"><span class="coupon__save">Save</span><div class="coupon__amount">$50 OFF</div><p class="coupon__text" style="margin-top:10px">Air Conditioner install</p></div>
  </div>

  <h2 class="promise-head">OUR PROMISE TO YOU</h2>
  <ul class="promise">
    <li>We will Arrive on time or we will pay you $100</li>
    <li>Before any job begins you will know the exact price We will leave your place as clean as we arrived</li>
    <li>If there is a problem and its our fault we will fix it for free</li>
    <li>Provide a 12 month warranty on all parts</li>
    <li>We will provide friendly helpful service and advice</li>
  </ul>

  <footer class="footer">
    <span class="footer__label">Contact Us:</span>
    <span class="footer__phone"><svg width="20" height="16" viewBox="0 0 20 16"><path d="M1 6 Q10 -2 19 6 L16 8 L14 5 L6 5 L4 8Z M4 9 L16 9 L18 15 L2 15Z" fill="#fff"/></svg>0487 562 903</span>
    <span class="footer__web">www.Quillbrook.com.au</span>
    <div class="pay"><span>nexo</span><span>swiftpay</span><span>tapnet</span></div>
    <span class="legal">License: 58164 &nbsp; ABN: 61 208 359 772</span>
  </footer>
</section>

<section class="flyer flyer--back">
  <svg class="shape" width="450" height="955" viewBox="0 0 450 955">
    <path d="M0 0 L450 0 L450 85 C350 35 200 15 0 40Z" fill="var(--blue)"/>
    <path d="M0 40 C200 15 350 35 450 85 L450 92 C340 48 200 40 0 72Z" fill="var(--orange)"/>
    <path d="M0 840 C150 868 320 868 450 855 L450 955 L0 955Z" fill="var(--orange)"/>
    <path d="M0 853 C150 880 320 880 450 867 L450 955 L0 955Z" fill="var(--blue)"/>
  </svg>
  <div class="brand" style="top:120px"><span class="brand__name">Quillbrook</span><span class="brand__dot"></span></div>
  <h2 class="banner">Here is what some of my customers<br>have had to say</h2>

  <div class="testimonials">
    <figure class="review-item">
      <blockquote class="review"><span class="review__mark">“</span>Extremely professional...<br>Arrived when he said he would, sent through a written quote and was very reasonable. He also checked out our smoke detectors whist he was here. He installed 2 ceiling fans and an air conditioner. He cleaned up the mess and was very efficient. I will definitely use him again and recommend him to family and friends”</blockquote>
      <figcaption class="review__who">P.M – Stretton</figcaption>
    </figure>
    <figure class="review-item">
      <blockquote class="review"><span class="review__mark">“</span>Excellent service provider. He arrived on time with a call before arriving, than carried all jobs quickly and efficiently and left no mess at all. I will definitely recommend his service to others requiring an electrician. Thanks again!”</blockquote>
      <figcaption class="review__who">R.T – Greenslopes</figcaption>
    </figure>
    <figure class="review-item">
      <blockquote class="review"><span class="review__mark">“</span>Over the long weekend, I had problems with my power, not only did you pick up the first phone call but you came out at 5am to fix it. Love the fact you’re a 24hr service!”</blockquote>
      <figcaption class="review__who">K.L - Mount Gravatt</figcaption>
    </figure>
  </div>

  <footer class="footer">
    <span class="footer__label">Contact Us:</span>
    <span class="footer__phone"><svg width="20" height="16" viewBox="0 0 20 16"><path d="M1 6 Q10 -2 19 6 L16 8 L14 5 L6 5 L4 8Z M4 9 L16 9 L18 15 L2 15Z" fill="#fff"/></svg>0487 562 903</span>
    <span class="footer__web">www.Quillbrook.com.au</span>
    <div class="pay"><span>nexo</span><span>swiftpay</span><span>tapnet</span></div>
    <span class="legal">License: 58164 &nbsp; ABN: 61 208 359 772</span>
  </footer>
</section>

</body>
</html>
```